Brisk Hounds Dog Behaviour, Training and Natural Healthcare Business Card Design

I am an experienced and qualified dog behavioural trainer and natural animal healthcare consultant offering a range of services to help pet dog owners with the "whole dog".
COLOURS: A soft light blue in the background - can be fading out or split, red should also feature
LOGO: Dog, healing hands, silhouette, shadow
SERVICES: Behaviour Consults, Training, Complex Skills Coaching Walking Coaching, Diet & Nutrition, Environmental Enrichment, Lifestyle and Lifestage Adaptations, Massage, Natural Health Options
BY LINE: Happy Dogs, Happy Owners
VALUES: Promoting communication and connection between dogs and their owners.
FOCUS: Nutritional guidance and environmental adaptation are often needed to complete the package and increase the success rate of training and behaviour modification.

Target Market(s)

Everyone who has a dog who they wish to improve their relationship with

Industry/Entity Type

Communication

Contact Information for Business Card

Brisk Hounds, Renata Walcott, 0472 680351, briskhounds7@mailnest.example, www.briskhounds7.example, Qualified Dog Behavioural Trainer and Natural Animal Healthcare Consultant

Font styles to use
Sans Serif
Script

Colors
85cae6
ec2027

Requirements
Must have
• A clear indication that it is a dog services business. A raised feature
Should not have
• Pawprints, cartoons

```html
<!DOCTYPE html>
<html lang="en">
<head>
<meta charset="utf-8">
<title>Brisk Hounds – Business Card Options</title>
<link rel="stylesheet" href="https://fonts.googleapis.com/css2?family=Archivo+Black&family=Tinos:wght@400;700&display=swap">
<style>
  :root {
    --page: #ffffff;
    --sky-top: #5fb4dc;
    --sky-mid: #a9dcef;
    --band: #eef8fc;
    --deep-top: #4aa3d3;
    --deep-bottom: #2a6fb8;
    --brand-red: #e2452b;
    --brand-red-dark: #8a1a10;
    --ink: #101820;
    --name-ink: #e9f4fa;
    --contact-ink: #ffffff;
    --slogan: #f08a1c;
    --photo-light: #f3eadb;
    --photo-mid: #c99a62;
    --photo-dark: #6b4a2c;
  }
  * { box-sizing: border-box; margin: 0; padding: 0; }
  html, body { width: 1200px; height: 362px; overflow: hidden; background: var(--page); }
  .sheet { position: relative; width: 1200px; height: 362px; }

  .card {
    position: absolute; top: 57px; width: 370px; height: 235px; overflow: hidden;
    background: linear-gradient(180deg, var(--sky-top) 0%, var(--sky-mid) 34%, var(--band) 44%, var(--band) 58%, var(--deep-top) 64%, var(--deep-bottom) 100%);
    box-shadow: 3px 4px 6px rgba(0,0,0,.35);
    font-family: "Tinos", "Times New Roman", serif;
  }
  .card--logo { left: 16px; }
  .card--photo-small { left: 406px; }
  .card--photo-large { left: 796px; }

  .card__waves { position: absolute; left: 0; bottom: 0; width: 100%; height: 90px; }

  .card__title {
    position: absolute; top: 15px; left: 0; width: 370px; text-align: center; white-space: nowrap;
    font-family: "Archivo Black", "Arial Black", sans-serif; font-size: 23px; letter-spacing: .5px;
    color: var(--brand-red); -webkit-text-stroke: 1px var(--brand-red-dark);
    text-shadow: 1px 2px 2px rgba(0,0,0,.35);
  }
  .card__name {
    position: absolute; top: 45px; left: 0; width: 370px; text-align: center; white-space: nowrap;
    font-size: 13px; letter-spacing: 1.5px; text-transform: uppercase; color: var(--name-ink);
    -webkit-text-stroke: .5px #244a66;
  }
  .card__role {
    position: absolute; top: 66px; left: 12px; width: 346px; text-align: center; white-space: nowrap;
    font-weight: 700; font-size: 9.6px; line-height: 15px; text-transform: uppercase; color: var(--ink);
  }
  .card__services {
    position: absolute; top: 99px; left: 14px; white-space: nowrap;
    font-size: 10.5px; line-height: 15.5px; font-variant: small-caps; color: var(--ink);
  }
  .card__contact { position: absolute; left: 14px; top: 153px; color: var(--contact-ink); font-size: 11px; white-space: nowrap; }
  .card__contact p { line-height: 17px; }
  .card__contact .label { display: inline-block; width: 44px; }
  .card__contact .phone { font-size: 12.5px; }
  .card__contact .email { margin-top: 4px; }

  .card__slogan {
    position: absolute; left: 168px; top: 166px; font-family: "Archivo Black", "Arial Black", sans-serif;
    font-size: 9px; line-height: 12px; color: var(--slogan); text-transform: uppercase; white-space: nowrap;
  }

  .card__brandmark {
    position: absolute; left: 262px; top: 130px; width: 100px; height: 90px;
    display: flex; flex-direction: column; align-items: center; justify-content: center; gap: 6px;
  }
  .card__brandmark-dot { width: 16px; height: 16px; border-radius: 50%; background: var(--slogan); }
  .card__brandmark-name { font-size: 12px; font-weight: 700; color: var(--slogan); white-space: nowrap; }

  .card__photo { position: absolute; }
  .card--photo-small .card__photo {
    left: 254px; top: 82px; width: 116px; height: 153px;
    background: radial-gradient(ellipse at 45% 40%, var(--photo-light) 0%, var(--photo-mid) 60%, var(--photo-dark) 100%);
  }
  .card--photo-large .card__photo {
    left: 242px; top: 0; width: 128px; height: 235px;
    background: radial-gradient(ellipse at 40% 45%, var(--photo-light) 0%, var(--photo-mid) 62%, var(--photo-dark) 100%);
  }

  .card--photo-large .card__title { width: 240px; font-size: 20px; }
  .card--photo-large .card__name { width: 240px; font-size: 12px; letter-spacing: 1px; }
  .card--photo-large .card__role { left: 4px; width: 234px; font-size: 8.2px; }
  .card--photo-large .card__services { top: 104px; font-size: 9px; line-height: 14.5px; }
  .card--photo-large .card__contact { top: 160px; }
  .card--photo-large .card__contact .email { margin-top: -1px; }
  .card--photo-large .card__slogan { left: 160px; top: 180px; }
</style>
</head>
<body>
<main class="sheet">

  <section class="card card--logo">
    <svg class="card__waves" viewBox="0 0 370 90" preserveAspectRatio="none" aria-hidden="true">
      <path d="M0 40 C90 10 200 70 370 30" fill="none" stroke="#bfe6f6" stroke-width="1" opacity=".6"/>
      <path d="M0 60 C120 35 220 85 370 50" fill="none" stroke="#bfe6f6" stroke-width="1" opacity=".5"/>
    </svg>
    <h1 class="card__title">BRISK HOUNDS</h1>
    <p class="card__name">Renata Walcott</p>
    <p class="card__role">Qualified Dog Behavioural Trainer and Natural Animal<br>Healthcare Consultant</p>
    <p class="card__services">Behaviour Consults, Training, Complex Skills,<br>Walking Coaching, Diet &amp; Nutrition, Adaptations,<br>Massage, Natural Health Options</p>
    <div class="card__contact">
      <p class="phone"><span class="label">Phone</span>0472 680351</p>
      <p>www.briskhounds7.example</p>
      <p class="email">briskhounds7@mailnest.example</p>
    </div>
    <p class="card__slogan">Happy Dogs,<br>Happy Owners</p>
    <div class="card__brandmark">
      <span class="card__brandmark-dot"></span>
      <span class="card__brandmark-name">Brisk Hounds</span>
    </div>
  </section>

  <section class="card card--photo-small">
    <svg class="card__waves" viewBox="0 0 370 90" preserveAspectRatio="none" aria-hidden="true">
      <path d="M0 40 C90 10 200 70 370 30" fill="none" stroke="#bfe6f6" stroke-width="1" opacity=".6"/>
      <path d="M0 60 C120 35 220 85 370 50" fill="none" stroke="#bfe6f6" stroke-width="1" opacity=".5"/>
    </svg>
    <h1 class="card__title">BRISK HOUNDS</h1>
    <p class="card__name">Renata Walcott</p>
    <p class="card__role">Qualified Dog Behavioural Trainer and Natural Animal<br>Healthcare Consultant</p>
    <p class="card__services">Behaviour Consults, Training, Complex Skills,<br>Walking Coaching, Diet &amp; Nutrition, Adaptations,<br>Massage, Natural Health Options</p>
    <div class="card__contact">
      <p class="phone"><span class="label">Phone</span>0472 680351</p>
      <p>www.briskhounds7.example</p>
      <p class="email">briskhounds7@mailnest.example</p>
    </div>
    <p class="card__slogan">Happy Dogs,<br>Happy Owners</p>
    <div class="card__photo" role="img" aria-label="Photo of a smiling beagle with a dark collar"></div>
  </section>

  <section class="card card--photo-large">
    <svg class="card__waves" viewBox="0 0 370 90" preserveAspectRatio="none" aria-hidden="true">
      <path d="M0 40 C90 10 200 70 370 30" fill="none" stroke="#bfe6f6" stroke-width="1" opacity=".6"/>
      <path d="M0 60 C120 35 220 85 370 50" fill="none" stroke="#bfe6f6" stroke-width="1" opacity=".5"/>
    </svg>
    <h1 class="card__title">BRISK HOUNDS</h1>
    <p class="card__name">Renata Walcott</p>
    <p class="card__role">Qualified Dog Behavioural Trainer<br>and Natural Animal Healthcare Consultant</p>
    <p class="card__services">Behaviour Consults, Training, Complex Skills,<br>Walking Coaching, Diet &amp; Nutrition, Adaptations,<br>Massage, Natural Health Options</p>
    <div class="card__contact">
      <p class="phone"><span class="label">Phone</span>0472 680351</p>
      <p>www.briskhounds7.example</p>
      <p class="email">briskhounds7@mailnest.example</p>
    </div>
    <p class="card__slogan">Happy Dogs,<br>Happy Owners</p>
    <div class="card__photo" role="img" aria-label="Large close-up photo of a smiling beagle with a dark collar"></div>
  </section>

</main>
</body>
</html>
```